Design a poster that illustrates the six central pillars of our school district's efforts with students. The attached PDF outlines the six main competencies we aim for students to possess upon graduation. Each of the 6 has 3 bullet points for the poster as well. The title is "Profile of a Drifter". Our mascot is this attached winged wheel. The overall concept is that staff take kids when they are young and develop these 6 things when they graduate. Our colors are navy, red, and white. We will make this poster in a variety of sizes in offices, classrooms, and in digital spaces as well. On the PDF - ignore the column that says "Synthesis". That has nothing to do with this poster.

The district is Corvath Falls Public Schools https://www.corvath.k12.example.us/

```html
<!DOCTYPE html>
<html lang="en">
<head>
<meta charset="utf-8">
<title>Profile of a Drifter – Corvath Falls Public Schools</title>
<link href="https://fonts.googleapis.com/css2?family=Montserrat:wght@800&family=Nunito:wght@900&family=Lexend:wght@300;400&family=Playball&display=swap" rel="stylesheet">
<style>
  :root {
    --navy: #25304a;
    --navy-deep: #1d2740;
    --red: #8e1b22;
    --red-bright: #b3262d;
    --white: #ffffff;
    --ink: #2b2b33;
    --backdrop: #8a8a8a;
  }
  * { margin: 0; padding: 0; box-sizing: border-box; }
  html, body { width: 984px; height: 1200px; overflow: hidden; background: var(--backdrop); }
  .poster {
    position: absolute; left: 67px; top: 71px;
    width: 1378px; height: 1782px;
    transform: scale(0.6); transform-origin: top left;
    background: var(--white); overflow: hidden;
    font-family: "Lexend", sans-serif;
  }
  .backdrop { position: absolute; inset: 0; }
  .brand { position: absolute; left: 60px; top: 62px; display: flex; align-items: center; gap: 22px; color: var(--navy); white-space: nowrap; }
  .brand-dot { width: 90px; height: 90px; border-radius: 50%; background: var(--navy); }
  .brand-name { font-size: 28px; font-weight: 400; letter-spacing: .2px; }
  .brand-tag { font-size: 19px; font-weight: 400; margin-top: 4px; }
  .title-bubble { position: absolute; left: 45px; top: 382px; width: 603px; height: 308px; }
  .title-text {
    position: absolute; left: 0; top: 44px; width: 603px; text-align: center;
    font-family: "Montserrat", sans-serif; font-weight: 800; color: var(--white);
    font-size: 96px; line-height: 110px; letter-spacing: 1px;
  }
  .title-script {
    position: absolute; left: 0; top: 92px; width: 603px; text-align: center;
    font-family: "Playball", cursive; color: var(--red-bright); font-size: 78px;
  }
  .pillar { position: absolute; width: 620px; height: 290px; }
  .pillar-icon {
    position: absolute; left: 0; top: 0; width: 126px; height: 126px; border-radius: 50%;
    background: var(--navy); border: 4px solid var(--white); box-shadow: 0 0 0 4px var(--red);
    display: flex; align-items: center; justify-content: center; z-index: 2;
  }
  .pillar-icon svg { width: 74px; height: 74px; fill: none; stroke: var(--white); stroke-width: 2.4; stroke-linecap: round; stroke-linejoin: round; }
  .pillar-bar {
    position: absolute; left: 118px; top: 42px; width: 390px; height: 52px;
    background: linear-gradient(90deg, var(--red) 0%, var(--red-bright) 70%, var(--red) 100%);
    border-radius: 0 26px 26px 0; padding-left: 20px; white-space: nowrap;
    font-family: "Nunito", sans-serif; font-weight: 900; font-size: 43px; line-height: 52px; color: var(--white);
  }
  .pillar-points { position: absolute; left: 16px; top: 145px; display: flex; list-style: none; }
  .pillar-points li {
    position: relative; width: 196px; padding-left: 19px; padding-right: 12px; height: 140px;
    font-size: 17px; font-weight: 300; line-height: 21.6px; color: var(--ink);
    background-image: repeating-linear-gradient(180deg, var(--red-bright) 0 2px, transparent 2px 5px);
    background-size: 1.5px calc(100% - 22px); background-position: 5px 22px; background-repeat: no-repeat;
  }
  .pillar-points li::before {
    content: ""; position: absolute; left: -2px; top: 3px; width: 14px; height: 14px;
    border: 1.5px solid var(--red-bright); border-radius: 50%;
  }
  .pillar-points li::after {
    content: ""; position: absolute; left: 3px; top: 6px; width: 3px; height: 6px;
    border-right: 1.5px solid var(--red-bright); border-bottom: 1.5px solid var(--red-bright);
    transform: rotate(40deg);
  }
  .footer {
    position: absolute; left: 50px; top: 1697px; width: 1281px; height: 85px;
    background: var(--red); border-radius: 42px 42px 0 0;
    display: flex; align-items: center; justify-content: center;
    color: var(--white); font-size: 21px; font-weight: 400; white-space: nowrap;
  }
  .footer-item { display: flex; align-items: center; gap: 8px; padding: 0 18px; }
  .footer-item + .footer-item { border-left: 1.5px solid rgba(255,255,255,.8); height: 62px; }
  .footer-item svg { width: 22px; height: 22px; flex: none; fill: none; stroke: var(--white); stroke-width: 2; }
</style>
</head>
<body>
<div class="poster">
  <svg class="backdrop" viewBox="0 0 1378 1782" width="1378" height="1782">
    <defs>
      <linearGradient id="sky" x1="0" y1="0" x2="0" y2="1">
        <stop offset="0" stop-color="#4f5266"/>
        <stop offset=".28" stop-color="#b46a4a"/>
        <stop offset=".4" stop-color="#f39a2c"/>
        <stop offset=".48" stop-color="#6a3420"/>
        <stop offset=".75" stop-color="#23150f"/>
        <stop offset="1" stop-color="#0d0a0a"/>
      </linearGradient>
      <radialGradient id="floor" cx=".5" cy=".45" r=".6">
        <stop offset="0" stop-color="#ffffff"/>
        <stop offset="1" stop-color="#eeeef1"/>
      </radialGradient>
    </defs>
    <rect width="1378" height="1782" fill="url(#floor)"/>
    <path role="img" aria-label="Photo: a graduate in cap and gown holding a young child's hand at sunset"
          d="M0,215 C300,235 640,160 820,0 H1378 V900 C1200,700 950,545 700,538 C450,532 200,570 0,600 Z" fill="url(#sky)"/>
    <path d="M0,220 C300,242 650,165 826,0" fill="none" stroke="#cfd0d6" stroke-width="3"/>
    <path d="M430,214 C610,195 720,110 762,0" fill="none" stroke="var(--navy)" stroke-width="7"/>
    <path d="M640,536 C950,540 1210,700 1378,890 V975 C1210,770 960,575 640,536 Z" fill="var(--navy)"/>
    <path d="M0,598 C80,585 160,578 240,572 C150,595 60,635 0,685 Z" fill="var(--red)"/>
  </svg>

  <div class="brand">
    <div class="brand-dot"></div>
    <div>
      <div class="brand-name">Corvath Falls Public Schools</div>
      <div class="brand-tag">Excellence in Academics, Arts &amp; Athletics</div>
    </div>
  </div>

  <div class="title-bubble">
    <svg viewBox="0 0 603 360" width="603" height="360" style="position:absolute;left:0;top:0">
      <path d="M80,0 H523 A80,80 0 0 1 603,80 V228 A80,80 0 0 1 523,308 H170 L101,358 V308 H80 A80,80 0 0 1 0,228 V80 A80,80 0 0 1 80,0 Z" fill="var(--navy)"/>
    </svg>
    <div class="title-text">PROFILE<br>DRIFTER</div>
    <div class="title-script">of a</div>
  </div>

  <section class="pillar" style="left:71px;top:767px">
    <div class="pillar-icon"><svg viewBox="0 0 48 48"><rect x="6" y="6" width="22" height="14" rx="3"/><path d="M12 20 l-2 5 6-5"/><rect x="24" y="12" width="18" height="12" rx="3"/><circle cx="14" cy="32" r="4"/><circle cx="34" cy="32" r="4"/><path d="M6 44 c0-6 16-6 16 0 M26 44 c0-6 16-6 16 0"/></svg></div>
    <h2 class="pillar-bar">Communicator</h2>
    <ul class="pillar-points">
      <li>Expresses ideas clearly and respectfully (written &amp; verbal).</li>
      <li>Listens actively and understands diverse perspectives.</li>
      <li>Adjusts communication to suit the audience and context.</li>
    </ul>
  </section>

  <section class="pillar" style="left:710px;top:773px">
    <div class="pillar-icon"><svg viewBox="0 0 48 48"><circle cx="24" cy="24" r="7"/><circle cx="24" cy="24" r="12" stroke-dasharray="4 3"/><path d="M24 4 a20 20 0 0 1 19 14 M24 44 a20 20 0 0 1 -19 -14"/><rect x="20" y="1" width="7" height="6"/><path d="M40 36 l4 7 h-8 z"/><circle cx="8" cy="12" r="3"/></svg></div>
    <h2 class="pillar-bar">Adaptable</h2>
    <ul class="pillar-points">
      <li>Responds productively to new situations, challenges, and constructive feedback.</li>
      <li>Learns from new experiences and applies prior knowledge in an ever-changing world.</li>
      <li>Adjusts behavior and approach to engage effectively with diverse groups and environments.</li>
    </ul>
  </section>

  <section class="pillar" style="left:71px;top:1069px">
    <div class="pillar-icon"><svg viewBox="0 0 48 48"><path d="M22 44 V36 h-6 v-6 l-4-2 4-6 c0-10 8-16 16-16 s12 6 12 14 c0 6-4 10-6 12 v8"/><circle cx="30" cy="18" r="5"/><circle cx="9" cy="20" r="4"/><path d="M9 24 v16 M9 32 h4 M9 37 h4"/></svg></div>
    <h2 class="pillar-bar">Critical Thinker</h2>
    <ul class="pillar-points">
      <li>Questions, analyzes, and evaluates information from multiple sources.</li>
      <li>Identifies and solves complex problems creatively.</li>
      <li>Uses evidence and diverse perspectives to form reasoned conclusions and make informed decisions.</li>
    </ul>
  </section>

  <section class="pillar" style="left:710px;top:1071px">
    <div class="pillar-icon"><svg viewBox="0 0 48 48"><rect x="18" y="4" width="12" height="10" rx="2"/><path d="M18 14 v12 M30 14 v12 M6 30 l10-8 8 8 8-8 10 8 M6 30 l8 12 M42 30 l-8 12"/><circle cx="24" cy="30" r="16" stroke-dasharray="2 4"/></svg></div>
    <h2 class="pillar-bar">Collaborator</h2>
    <ul class="pillar-points">
      <li>Demonstrates strong teamwork by contributing effectively and cooperatively toward shared goals.</li>
      <li>Listens actively and values diverse ideas and perspectives.</li>
      <li>Engages respectfully, knowing when to compromise, support, or take the lead.</li>
    </ul>
  </section>

  <section class="pillar" style="left:71px;top:1371px">
    <div class="pillar-icon"><svg viewBox="0 0 48 48"><circle cx="25" cy="15" r="8"/><path d="M21 15 l3 3 5-6"/><path d="M4 34 l8-4 h10 c3 0 3 4 0 4 h-7 M22 34 l14-6 c3-1 5 2 2 4 l-14 10 H12 l-8-4"/></svg></div>
    <h2 class="pillar-bar">Responsible</h2>
    <ul class="pillar-points">
      <li>Takes ownership of actions, choices, and commitments now and in future aspirations.</li>
      <li>Takes pride in managing time, resources, and self while striving to meet high expectations.</li>
      <li>Acts with integrity while advocating for themselves and others.</li>
    </ul>
  </section>

  <section class="pillar" style="left:710px;top:1371px">
    <div class="pillar-icon"><svg viewBox="0 0 48 48"><path d="M24 34 l-8-8 c-3-3 0-8 4-6 l4 3 4-3 c4-2 7 3 4 6 z"/><path d="M8 8 v20 l8 14 M40 8 v20 l-8 14 M12 12 v14 M36 12 v14"/></svg></div>
    <h2 class="pillar-bar">Compassionate</h2>
    <ul class="pillar-points">
      <li>Understands and acknowledges others' feelings, perspectives, and experiences.</li>
      <li>Responds with kindness, patience, empathy, and support.</li>
      <li>Seeks to connect with others and contribute positively to their well-being and the community's well-being.</li>
    </ul>
  </section>

  <footer class="footer">
    <div class="footer-item"><svg viewBox="0 0 24 24"><path d="M12 22 s-7-7-7-12 a7 7 0 0 1 14 0 c0 5-7 12-7 12z"/><circle cx="12" cy="10" r="2.5"/></svg>Corvath Falls Public Schools 48 Alder Ridge Rd.</div>
    <div class="footer-item"><svg viewBox="0 0 24 24"><circle cx="12" cy="12" r="10"/><path d="M2 12 h20 M12 2 c-5 6-5 14 0 20 M12 2 c5 6 5 14 0 20"/></svg>www.corvath.k12.example.us</div>
    <div class="footer-item"><svg viewBox="0 0 24 24"><path d="M5 3 h4 l2 5 -3 2 c1 3 3 5 6 6 l2-3 5 2 v4 c0 1-1 2-2 2 C10 21 3 14 3 5 c0-1 1-2 2-2z"/></svg>555-014-2290</div>
  </footer>
</div>
</body>
</html>
```